Security Officer Training Certifications POSTCARD

We need Post Card Design
-Front and Back
-In Compliance with TORLEN HUB for upload!
-For Oversized and Jumbo Size Cards (torlen hubs)
Our Company:
www.ashworthmaplebrookinstitute.org (FOR IDEAS)
We provide Corporate Security Officer/Criminal Justice/Police Tactics Training for Private Companies that have a security department and officers.
We provide:
Handcuffing certifications
Pepper Spray
Compliance Training
Instructor Training
California Guard Card
Our Card to display powerful image for a Security Officer Department
Traits in Pic and Deigns
VALUE
COMPETITIVE EDGE
PROFESSIONAL GROWTH
QUALITY
PROFICIENT/EFFECTIVE SECURITY OFFICERS
TACTICAL OFFICERS
PROFESSIONALISM
EXPERTS
INDUSTRY LEADERS
READINESS
FRONT DESIGN TO BE VERY CATCH AND ATTRACTIVE!
-Please put the images of lawn enforcement, security guards, public safety department in the FRONT
BACK OF THE CARD DESIGN
-Please put our Services/Menu, CREATIVE and CATCHY, in columns and with vivid colors.

```html
<!DOCTYPE html>
<html lang="en">
<head>
<meta charset="utf-8">
<title>Security Officer Training Postcard</title>
<link rel="stylesheet" href="https://fonts.googleapis.com/css2?family=Lato:wght@400;700&family=Archivo+Black&display=swap">
<style>
  :root {
    --red: #a81d2b;
    --red-deep: #8c1520;
    --ink: #222326;
    --muted: #555a60;
    --paper: #ffffff;
    --mist: #eceded;
    --stage: #d8d9db;
    --stamp: #9b9b9b;
    --rule: #a5a7aa;
  }
  * { box-sizing: border-box; margin: 0; padding: 0; }
  html, body { width: 1200px; height: 1200px; overflow: hidden; }
  body {
    background: var(--stage);
    font-family: "Lato", sans-serif;
    color: var(--ink);
    position: relative;
  }
  .postcard {
    position: absolute;
    width: 1015px;
    height: 657px;
    overflow: hidden;
    background: var(--paper);
    transform-origin: 0 0;
    transform: scale(0.8);
    box-shadow: 0 6px 18px rgba(0,0,0,.25);
  }
  .postcard--front { left: 74px; top: 42px; }
  .postcard--back { left: 276px; top: 618px; height: 658px; }

  /* FRONT */
  .front-bg-lower {
    position: absolute; left: 0; top: 275px; width: 100%; height: 382px;
    background: linear-gradient(100deg, #ffffff 0%, #f6f6f6 55%, #e3e4e6 100%);
  }
  .front-bg-upper {
    position: absolute; left: 0; top: 0; width: 100%; height: 275px;
    background: linear-gradient(180deg, var(--red) 0%, #9d1a27 75%, var(--red-deep) 100%);
  }
  .hero-photo {
    position: absolute; left: 598px; top: -128px; width: 540px; height: 540px;
    border-radius: 50%;
    border: 14px solid var(--red);
    background: linear-gradient(90deg, #cfd8dc 0%, #7fc4e8 30%, #5cb2df 55%, #26303d 75%, #1b222c 100%);
  }
  .partner-badges { position: absolute; left: 100px; top: 53px; display: flex; gap: 35px; }
  .partner-badge {
    width: 73px; height: 82px; background: var(--paper);
    display: flex; align-items: center; justify-content: center;
  }
  .partner-badge span { width: 46px; height: 52px; border-radius: 50%; background: #c9b98a; }
  .partner-badge--dark { background: #111; }
  .partner-badge--dark span { background: #2c4a7a; }
  .partner-badge--red span { background: var(--red); border-radius: 6px; }
  .partner-badge--steel span { background: #9aa3ad; border-radius: 4px 4px 50% 50%; }
  .service-photo {
    position: absolute; width: 156px; height: 156px; border-radius: 50%;
    border: 4px solid var(--paper);
    box-shadow: 0 2px 6px rgba(0,0,0,.3);
  }
  .service-photo--monitoring { left: 42px; top: 196px; background: radial-gradient(circle at 60% 35%, #a9c8e6, #3c5f86 60%, #1f2c40); }
  .service-photo--fire { left: 233px; top: 196px; background: radial-gradient(circle at 50% 50%, #ffd35a, #f07a18 45%, #7a2a0c 80%); }
  .service-photo--control { left: 430px; top: 192px; background: radial-gradient(circle at 50% 40%, #3a5d8a, #7fb5dc 55%, #e8eef2); }
  .front-headline { position: absolute; left: 68px; top: 406px; font-size: 24px; font-weight: 700; }
  .front-services { position: absolute; left: 50px; top: 455px; display: flex; gap: 22px; list-style: none; font-size: 23px; }
  .front-services li::before { content: "●"; color: var(--red); font-size: 15px; margin-right: 10px; vertical-align: 3px; }
  .audience-pill {
    position: absolute; left: 55px; top: 520px; width: 758px; height: 47px;
    border-radius: 24px; border: 1px solid #c8c9cb;
    background: linear-gradient(180deg, #ffffff, #e9eaeb);
    box-shadow: 0 2px 4px rgba(0,0,0,.15);
    font-size: 22px; line-height: 45px; padding-left: 17px;
  }
  .front-footer {
    position: absolute; left: 0; top: 603px; width: 100%; height: 49px;
    background: var(--red-deep); color: var(--paper);
    font-size: 17px; letter-spacing: 3.6px; text-align: center; line-height: 49px;
  }

  /* BACK */
  .back-bg {
    position: absolute; inset: 0;
    background: linear-gradient(100deg, #ffffff 0%, #ffffff 35%, #ececed 70%, #e2e3e4 100%);
  }
  .portrait-ring {
    position: absolute; left: -40px; top: -90px; width: 440px; height: 450px;
    border-radius: 50%; background: var(--red);
  }
  .portrait-photo {
    position: absolute; left: -55px; top: -77px; width: 440px; height: 440px;
    border-radius: 50%; border: 5px solid var(--paper);
    background: linear-gradient(180deg, #6c6e72 0%, #8d9095 50%, #b5b9bf 100%);
  }
  .back-heading { position: absolute; left: 55px; top: 394px; font-size: 23px; font-weight: 700; color: var(--red); }
  .back-services { position: absolute; left: 58px; top: 423px; list-style: none; font-size: 19.5px; line-height: 24px; color: #333; }
  .back-services li::before { content: "•"; color: var(--red); margin-right: 9px; }
  .watermark {
    position: absolute; left: 433px; top: 352px;
    font-family: "Archivo Black", sans-serif; font-size: 118px; line-height: 1;
    letter-spacing: 0; white-space: nowrap;
    transform-origin: 0 0; transform: scaleX(0.7);
    color: rgba(255,255,255,.75);
  }
  .stamp-box { position: absolute; left: 865px; top: 41px; width: 92px; height: 92px; background: var(--stamp); }
  .address-line { position: absolute; left: 617px; width: 356px; height: 2px; background: var(--rule); }
  .back-footer {
    position: absolute; left: 0; top: 573px; width: 100%; height: 63px;
    background: var(--red-deep); color: var(--paper); font-size: 16px;
  }
  .contact { position: absolute; display: flex; align-items: flex-start; gap: 8px; white-space: nowrap; }
  .contact svg { flex: none; margin-top: 2px; }
  .contact--phone { left: 55px; top: 22px; }
  .contact--web { left: 230px; top: 22px; }
  .contact--place { left: 560px; top: 11px; line-height: 20px; }
</style>
</head>
<body>

<section class="postcard postcard--front">
  <div class="front-bg-lower"></div>
  <div class="front-bg-upper"></div>
  <div class="hero-photo" role="img" aria-label="Security officer in light blue shirt with a radio clipped to his belt"></div>

  <div class="partner-badges">
    <div class="partner-badge"><span></span></div>
    <div class="partner-badge partner-badge--dark"><span></span></div>
    <div class="partner-badge partner-badge--red"><span></span></div>
    <div class="partner-badge partner-badge--steel"><span></span></div>
  </div>

  <div class="service-photo service-photo--monitoring" role="img" aria-label="Operator watching surveillance screens"></div>
  <div class="service-photo service-photo--fire" role="img" aria-label="Firefighter in gear surrounded by flames"></div>
  <div class="service-photo service-photo--control" role="img" aria-label="Officer at a control room video wall"></div>

  <h1 class="front-headline">We provide Corporate Security</h1>
  <ul class="front-services">
    <li>Security Officer</li>
    <li>Criminal Justice</li>
    <li>Police Tactics Training</li>
  </ul>
  <p class="audience-pill">for Private Companies that have a security department and officers.</p>
  <footer class="front-footer">www.ashworthmaplebrookinstitute.org</footer>
</section>

<section class="postcard postcard--back">
  <div class="back-bg"></div>
  <div class="watermark">SECURITY</div>
  <div class="portrait-ring"></div>
  <div class="portrait-photo" role="img" aria-label="Uniformed security guard speaking into a radio in front of city towers"></div>

  <h2 class="back-heading">We provide:</h2>
  <ul class="back-services">
    <li>Handcuffing certifications</li>
    <li>Pepper Spray</li>
    <li>Compliance Training</li>
    <li>Instructor Training</li>
    <li>California Guard Card</li>
  </ul>

  <div class="stamp-box"></div>
  <div class="address-line" style="top:277px"></div>
  <div class="address-line" style="top:327px"></div>
  <div class="address-line" style="top:382px"></div>
  <div class="address-line" style="top:430px"></div>

  <footer class="back-footer">
    <div class="contact contact--phone">
      <svg width="17" height="17" viewBox="0 0 24 24"><path fill="#fff" d="M6.6 10.8a15 15 0 0 0 6.6 6.6l2.2-2.2c.3-.3.7-.4 1-.2 1.1.4 2.3.6 3.6.6.6 0 1 .4 1 1V20c0 .6-.4 1-1 1A17 17 0 0 1 3 4c0-.6.4-1 1-1h3.5c.6 0 1 .4 1 1 0 1.3.2 2.5.6 3.6.1.3 0 .7-.2 1z"/></svg>
      <span>(555) 014-2290</span>
    </div>
    <div class="contact contact--web">
      <svg width="18" height="18" viewBox="0 0 24 24" fill="none" stroke="#fff" stroke-width="2"><circle cx="12" cy="12" r="9"/><path d="M3 12h18M12 3c3 3 3 15 0 18M12 3c-3 3-3 15 0 18"/></svg>
      <span>www.ashworthmaplebrookinstitute.org</span>
    </div>
    <div class="contact contact--place">
      <svg width="14" height="19" viewBox="0 0 14 20"><path fill="#fff" d="M7 0a7 7 0 0 0-7 7c0 5 7 13 7 13s7-8 7-13a7 7 0 0 0-7-7zm0 9.5A2.5 2.5 0 1 1 7 4.5a2.5 2.5 0 0 1 0 5z"/></svg>
      <span>City Of Redfield, Harlow and East Harlow cities<br>2150 N. Orchard Ave Redfield, CA 90001</span>
    </div>
  </footer>
</section>

</body>
</html>
```